Modernising a Traditional Image - Wrenfold Silver Band

The Brass Band musical world in Britain is under threat. It is a wonderful place for children and amateurs to learn a musical instrument - it is our responsibility to protect it and grow it.
We can have a combined image of being old and slow. Our organisation wants to celebrate youth and a new / innovative way of doing things.

We don't wish to create a new logo as that exists now on our rather expensive uniforms - BUT to provide an attractive message for potential young players, something that we can use on Roll-up Banners, Facebook posts, Web banners, Tickets, Concert programmes. In short a cohesive image for our communication. I have however included the Logo design - so perhaps preparing the road for a future logo transition, or perhaps for use with the Wrenfold Academy / Training Band.

UPDATE TO BRIEF 26/08 - DO NOT PLEASE INCLUDE THE OLD LOGO AT ALL. THINK NEW, THINK BOLD, THINK BRIGHT, YOUNG, ETC.

The final designs need to communicate a basis of tradition, but a bright, young innovative future. Please consider the bright brass bands in UK (https://www.instagram.com/qelrvh/), and those in the Netherlands, Scandinavia, etc.

Current website / socials:
https://www.facebook.com/Wrenfoldband
https://www.facebook.com/NorthCragley
https://www.wrenfold.band/

Target Market(s)

Young learners of musical instrument. Followers of music events, theatre, et.

Industry/Entity Type

Music theatre education

Requirements
Must have
• An invite.. 'come witness the magic being made at Band Practice Thursdays'.. as an example
Nice to have
• Bright colour (not linked to current logo). Surprise me
Should not have
• Any link to old logo

```html
<!DOCTYPE html>
<html lang="en">
<head>
<meta charset="utf-8">
<title>Wrenfold Silver Band – Music, the Original Wonder Drug</title>
<link rel="stylesheet" href="https://fonts.googleapis.com/css2?family=Montserrat:wght@300;400;500;600;700;800&display=swap">
<style>
  :root {
    --purple: #5a1d85;
    --yellow: #fff200;
    --yellow-strip: #ffff00;
    --white: #ffffff;
    --brass-light: #f7a93a;
    --brass-mid: #ef8d1c;
    --brass-dark: #c96a12;
  }
  * { box-sizing: border-box; margin: 0; padding: 0; }
  html, body {
    width: 1200px;
    height: 1200px;
    overflow: hidden;
  }
  body {
    font-family: "Montserrat", Arial, sans-serif;
    background: var(--yellow-strip);
  }
  .poster {
    position: relative;
    width: 1200px;
    height: 1200px;
    background: var(--yellow-strip);
    overflow: hidden;
  }
  .poster__panel {
    position: absolute;
    left: 0; top: 0;
    width: 866px;
    height: 1200px;
    background: var(--purple);
  }
  .poster__instruments {
    position: absolute;
    left: 806px;
    top: 80px;
    width: 394px;
    height: 900px;
    border-radius: 200px 0 0 200px;
    background: linear-gradient(160deg, var(--brass-light) 0%, var(--brass-mid) 55%, var(--brass-dark) 100%);
  }
  .copy { position: relative; z-index: 1; }
  .headline {
    position: absolute;
    left: 89px;
    top: 70px;
    color: var(--yellow);
    font-weight: 700;
    font-size: 152px;
    line-height: 1;
    letter-spacing: -2px;
  }
  .subhead {
    position: absolute;
    left: 89px;
    top: 264px;
    color: var(--white);
    font-weight: 700;
    font-size: 68px;
    line-height: 1;
  }
  .tagline {
    position: absolute;
    left: 89px;
    top: 350px;
    color: var(--white);
    font-weight: 300;
    font-size: 73px;
    line-height: 89px;
    letter-spacing: 2px;
    white-space: nowrap;
  }
  .divider {
    position: absolute;
    left: 87px;
    top: 642px;
    width: 655px;
    height: 5px;
    background: var(--white);
  }
  .cta-title {
    position: absolute;
    left: 87px;
    top: 690px;
    color: var(--yellow);
    font-weight: 600;
    font-size: 49px;
    line-height: 1;
    white-space: nowrap;
  }
  .cta-sub {
    position: absolute;
    left: 89px;
    top: 750px;
    color: var(--white);
    font-weight: 300;
    font-size: 36px;
    line-height: 1;
    letter-spacing: 1.5px;
    white-space: nowrap;
  }
  .side-effects {
    position: absolute;
    left: 90px;
    top: 812px;
    color: var(--white);
    font-weight: 400;
    font-size: 22.5px;
    line-height: 32px;
    white-space: nowrap;
  }
  .invite {
    position: absolute;
    left: 87px;
    top: 1004px;
    width: 663px;
    height: 119px;
    background: var(--yellow);
    color: var(--purple);
    text-align: center;
    padding-top: 18px;
  }
  .invite__lead {
    display: block;
    font-weight: 400;
    font-size: 27px;
    line-height: 1.2;
  }
  .invite__event {
    display: block;
    font-weight: 700;
    font-size: 43px;
    line-height: 1.2;
  }
  .brand {
    position: absolute;
    left: 888px;
    top: 1022px;
    display: flex;
    align-items: center;
    gap: 12px;
    color: var(--purple);
  }
  .brand__mark {
    width: 56px;
    height: 56px;
    border-radius: 50%;
    background: var(--purple);
    flex: none;
  }
  .brand__name {
    font-weight: 700;
    font-size: 25px;
    line-height: 1.05;
  }
</style>
</head>
<body>
  <main class="poster">
    <div class="poster__panel"></div>
    <div class="poster__instruments" role="img" aria-label="Illustration of three brass instruments: a French horn, a euphonium and a trumpet"></div>

    <div class="copy">
      <h1 class="headline">MUSIC</h1>
      <p class="subhead">THE ORIGINAL</p>
      <p class="tagline">MOOD-ALTERING,<br>NON-FATTENING,<br>WONDER DRUG,</p>

      <div class="divider"></div>

      <p class="cta-title">ASK YOUR DOCTOR</p>
      <p class="cta-sub">IF MUSIC IS RIGHT FOR YOU</p>

      <p class="side-effects">Common side effectives include, but are not limit-<br>ed to, spontaneous happiness, increased memory<br>&amp; motor function, connection to others, movement<br>of the feed &amp; head, &amp; the occasional persistence of<br>catchy melodies</p>

      <div class="invite">
        <span class="invite__lead">Come witness the magic being made at</span>
        <span class="invite__event">Band Practice Thursdays</span>
      </div>

      <div class="brand">
        <span class="brand__mark"></span>
        <span class="brand__name">WRENFOLD<br>SILVER BAND</span>
      </div>
    </div>
  </main>
</body>
</html>
```